WebSite Revamp / Modernize / stylize to draw in more customers to stay on site

Keel-Deck is looking for a website revamp - we had our old site for some time and now is the time for an update - current site - http://www.keel-deck-example.com/ For additional photos, head to the facebook page - https://www.facebook.com/keeldeckexample / I attached the entire current website as well - looking for something modern and bold that has guy appeal - this is not a cheap product and would like site to have that feel as well.

Target Market(s)

Fishermen, fishing guides, homeowners, boat owners

Coding

Coded - Design and coding required

Number of Pages Required

5+ page

Font styles to use
Serif
Sans Serif
Other font styles liked:
• logo font is "Niamey Medium"

Colors
3176b5
0255a3
3276b5
0692cd
33a6d7
85cae6
cee9f5
b1b1b1
d5d5d5

Requirements
Must have
• Keep colors inline with our logo (blues / greys). Also, need it to be relatively easy to add and remove new locations as they come online - we are franchising and starting to add new locations pretty quickly - need this to be an easy process/update to the site.
Nice to have
• Surprise me

```html
<!DOCTYPE html>
<html lang="en">
<head>
<meta charset="utf-8">
<title>Keel-Deck | High Performance Marine Surfacing</title>
<link href="https://fonts.googleapis.com/css2?family=Exo+2:wght@400;500;600&family=Montserrat:wght@400;500;600&display=swap" rel="stylesheet">
<style>
:root{
  --blue:#0255a3;
  --blue-mid:#3176b5;
  --blue-bright:#0692cd;
  --blue-soft:#85cae6;
  --ink:#1f2a36;
  --text:#6d727a;
  --grey:#b1b1b1;
  --line:#d5d5d5;
  --slate:#4b525b;
  --pale:#f3f4f6;
  --white:#fff;
}
*{box-sizing:border-box;margin:0;padding:0}
html,body{width:1200px;height:4138px;overflow:hidden;background:var(--white)}
body{position:relative;font-family:"Montserrat",sans-serif;color:var(--text)}
a{color:inherit;text-decoration:none}
.abs{position:absolute}
.head-font{font-family:"Exo 2",sans-serif}

/* header */
.site-header{position:absolute;left:0;top:0;width:1200px;height:150px}
.brand{position:absolute;left:28px;top:26px;display:flex;flex-direction:column;align-items:flex-start}
.brand-name{font-family:"Exo 2",sans-serif;font-weight:600;font-size:40px;color:var(--blue);line-height:1;display:flex;align-items:center;gap:10px}
.brand-name i{display:block;width:22px;height:22px;background:var(--blue-bright);border-radius:50%}
.brand-tag{font-family:"Exo 2",sans-serif;font-weight:600;font-size:14px;color:var(--blue);margin-top:8px}
.call{position:absolute;left:566px;top:40px;color:var(--blue-bright);font-size:17px;font-weight:500;display:flex;align-items:center;gap:8px}
.call-brace{position:absolute;left:660px;top:28px;width:20px;height:72px}
.locations{position:absolute;left:700px;top:36px;display:flex;gap:52px}
.loc{text-align:center}
.loc span{display:block;font-size:12px;letter-spacing:.5px;color:var(--ink)}
.loc b{display:block;font-size:17px;font-weight:600;color:var(--blue-bright);margin-top:12px}
.main-nav{position:absolute;right:36px;top:112px;display:flex;gap:46px;font-size:12px;font-weight:500;letter-spacing:1px;color:var(--ink)}
.main-nav .active{color:var(--blue-bright)}

/* hero */
.hero{position:absolute;left:0;top:150px;width:1200px;height:480px;background:linear-gradient(135deg,#5d6064 0%,#8d8e90 45%,#6e7073 70%,#c9cacc 100%)}
.hero-shade{position:absolute;inset:0;background:rgba(0,0,0,.18)}
.hero-title{position:absolute;left:300px;top:138px;width:600px;text-align:center;font-family:"Exo 2",sans-serif;font-weight:600;font-size:31px;line-height:1.22;color:var(--white)}
.btn{display:inline-block;background:var(--blue-bright);color:var(--white);font-size:11px;letter-spacing:1.5px;font-weight:600}
.hero .btn{position:absolute;left:530px;top:291px;width:140px;height:37px;line-height:37px;text-align:center}
.hero-arrow{position:absolute;top:218px;width:36px;height:36px;border-radius:50%;border:1.5px solid var(--white)}
.hero-arrow.prev{left:106px}
.hero-arrow.next{right:106px;background:var(--white)}
.hero-dots{position:absolute;left:561px;top:430px;display:flex;gap:10px}
.hero-dots i{width:9px;height:9px;border-radius:50%;background:rgba(255,255,255,.6)}
.hero-dots i.on{background:var(--white)}

/* common section titles */
.eyebrow{position:absolute;font-size:11px;font-weight:600;letter-spacing:1.2px;color:var(--blue-bright)}
.sec-title{position:absolute;font-family:"Exo 2",sans-serif;font-weight:500;font-size:32px;color:var(--ink)}
.link-more{position:absolute;font-size:11px;font-weight:600;letter-spacing:1px;color:var(--ink);padding-bottom:8px;border-bottom:2px solid var(--blue-bright)}

/* welcome */
.welcome-h{position:absolute;left:110px;top:800px;width:470px;font-family:"Exo 2",sans-serif;font-weight:500;font-size:30px;line-height:1.4;color:var(--ink)}
.welcome-h .rule{display:inline-block;width:110px;height:2px;background:var(--ink);vertical-align:middle;margin-left:12px}
.welcome-sub{position:absolute;left:110px;top:936px;width:470px;font-family:"Exo 2",sans-serif;font-size:27px;line-height:1.35;color:var(--ink)}
.welcome-p{position:absolute;left:110px;top:1024px;width:470px;font-size:13px;line-height:1.85}
.welcome-frame{position:absolute;left:764px;top:717px;width:376px;height:456px;border:2px solid var(--line)}
.welcome-photo{position:absolute;left:648px;top:767px;width:442px;height:461px;background:linear-gradient(160deg,#dfe3e6,#9aa1a7 55%,#c4c9cd)}

/* stats */
.stats{position:absolute;left:110px;top:1319px;width:980px;height:130px;border:1px solid #eceef0;background:#fbfcfd;display:flex}
.stat{flex:1;text-align:center;padding-top:30px}
.stat b{display:block;font-family:"Exo 2",sans-serif;font-weight:500;font-size:36px;color:var(--ink)}
.stat span{display:block;font-size:11px;letter-spacing:1px;color:var(--blue-bright);margin-top:8px}

/* services */
.service{position:absolute;left:110px;width:980px;height:352px}
.service .photo{position:absolute;top:0;width:483px;height:352px}
.service .panel{position:absolute;top:0;width:497px;height:352px;background:#fafbfc;border:1px solid #eef0f2}
.service .tag{position:absolute;font-size:11px;font-weight:600;letter-spacing:1px;color:var(--blue-bright)}
.service h3{position:absolute;font-family:"Exo 2",sans-serif;font-weight:600;font-size:21px;line-height:1.3;color:var(--ink)}
.service p{position:absolute;font-size:13px;line-height:1.8}
.service-marine{top:1631px}
.service-marine .photo{left:0;background:linear-gradient(150deg,#8c9197,#c8ccd0 45%,#6f757b)}
.service-marine .panel{left:483px}
.service-marine .connector{position:absolute;left:440px;top:45px;width:80px;height:1.5px;background:var(--blue-bright)}
.service-residential{top:2039px}
.service-residential .photo{left:497px;background:linear-gradient(140deg,#c9bda9,#8f7f68 50%,#3c4a3a)}
.service-residential .panel{left:0}

/* gallery */
.proj{position:absolute;top:2574px;height:353px}
.proj-left{left:0;width:251px;background:linear-gradient(160deg,#d9d6cf,#a9a59c)}
.proj-main{left:279px;width:642px;background:linear-gradient(150deg,#4e6b4a,#97a39a 50%,#5d6560)}
.proj-main .shade{position:absolute;inset:0;background:linear-gradient(0deg,rgba(0,0,0,.45),rgba(0,0,0,0) 60%)}
.proj-main .cat{position:absolute;left:58px;top:240px;font-size:11px;color:var(--white);letter-spacing:.5px}
.proj-main h4{position:absolute;left:58px;top:258px;font-family:"Exo 2",sans-serif;font-weight:600;font-size:22px;line-height:1.2;color:var(--white)}
.proj-main .plus{position:absolute;left:578px;top:278px;width:34px;height:34px;border-radius:50%;border:1.5px solid var(--white)}
.proj-right{left:949px;width:251px;background:linear-gradient(150deg,#d7d3ca,#b9b4a8)}

/* cta */
.cta-text{position:absolute;left:193px;top:3007px;font-family:"Exo 2",sans-serif;font-weight:600;font-size:22px;line-height:1.3;color:var(--blue)}
.cta-btn{position:absolute;left:864px;top:3017px;width:138px;height:46px;line-height:44px;text-align:center;border:1.5px solid var(--blue-soft);font-size:11px;letter-spacing:1.5px;color:var(--blue-bright);font-weight:600}

/* testimonials */
.testimonials{position:absolute;left:28px;top:3151px;width:1144px;height:394px;background:var(--slate);text-align:center;color:var(--white)}
.testimonials .eyebrow{position:relative;display:block;color:var(--white);padding-top:46px}
.testimonials h2{font-family:"Exo 2",sans-serif;font-weight:500;font-size:32px;margin-top:8px}
.testimonials blockquote{width:830px;margin:30px auto 0;font-size:17px;line-height:1.75;color:#e7e9ec}
.author{display:flex;justify-content:center;align-items:center;gap:18px;margin-top:40px;font-size:11px;letter-spacing:1px;color:var(--blue-soft)}
.author .dash{width:30px;height:1px;background:var(--grey)}
.view-all{display:inline-block;margin-top:32px;font-size:11px;letter-spacing:1px;color:var(--blue-soft);padding-bottom:6px;border-bottom:2px solid var(--blue-bright)}

/* links */
.links-rule{position:absolute;left:110px;top:3622px;width:980px;height:1px;background:#eceef0}
.links-label{position:absolute;left:0;width:1200px;top:3630px;text-align:center;font-size:11px;font-weight:600;letter-spacing:1.2px;color:var(--blue-bright)}
.links-title{position:absolute;left:0;width:1200px;top:3660px;text-align:center;font-family:"Exo 2",sans-serif;font-weight:500;font-size:32px;color:var(--ink)}
.partner{position:absolute;top:3725px;height:71px}
.partner-a{left:110px;width:312px;background:#3a5d8f}
.partner-b{left:474px;width:235px;background:#a08f6e}
.partner-c{left:756px;width:334px;background:#5a7aa8}

/* footer */
.site-footer{position:absolute;left:28px;top:3885px;width:1144px;height:253px;background:var(--pale)}
.foot-brand{position:absolute;left:60px;top:62px;font-family:"Exo 2",sans-serif;font-weight:600;font-size:30px;color:var(--blue);display:flex;align-items:center;gap:8px}
.foot-brand i{width:16px;height:16px;border-radius:50%;background:var(--blue-bright);display:block}
.foot-nav{position:absolute;left:346px;top:83px;display:flex;gap:40px;font-size:11px;font-weight:500;letter-spacing:1px;color:var(--ink)}
.social{position:absolute;left:1013px;top:70px;width:36px;height:36px;border-radius:50%;border:1.5px solid var(--blue-bright)}
.foot-rule{position:absolute;left:0;top:157px;width:1144px;height:1px;background:#e3e6ea}
.copyright{position:absolute;left:54px;top:184px;font-size:12px;color:var(--text)}
.copyright b{color:var(--blue-bright);font-weight:600}
.directions{position:absolute;left:416px;top:184px;font-size:11px;letter-spacing:1px;color:var(--blue);padding-bottom:6px;border-bottom:2px solid var(--blue-bright)}
.to-top{position:absolute;left:1017px;top:180px;width:24px;height:24px}
</style>
</head>
<body>

<header class="site-header">
  <a class="brand" href="http://www.keel-deck-example.com/">
    <span class="brand-name"><i></i>Keel-Deck</span>
    <span class="brand-tag">High Performance Marine Surfacing</span>
  </a>
  <div class="call">
    <svg width="18" height="18" viewBox="0 0 24 24" fill="none" stroke="currentColor" stroke-width="2"><path d="M5 3h4l2 5-3 2a12 12 0 0 0 6 6l2-3 5 2v4a2 2 0 0 1-2 2A17 17 0 0 1 3 5a2 2 0 0 1 2-2z"/></svg>
    Call Us:
  </div>
  <svg class="call-brace" viewBox="0 0 20 72" fill="none" stroke="#b1b1b1" stroke-width="1.5"><path d="M2 2c8 0 8 6 8 14v10c0 6 4 10 8 10-4 0-8 4-8 10v10c0 8 0 14-8 14"/></svg>
  <div class="locations">
    <div class="loc"><span>DICKINSON TX</span><b>555.201.3370</b></div>
    <div class="loc"><span>SOUTH TEXAS</span><b>555.342.8815</b></div>
    <div class="loc"><span>MISSISSIPPI</span><b>555.476.1290</b></div>
  </div>
  <nav class="main-nav">
    <a class="active" href="#">HOME</a><a href="#">MARINE</a><a href="#">RESIDENTIAL</a><a href="#">PHOTOS</a><a href="#">TESTIMONIALS</a><a href="#">FAQS</a><a href="#">LINKS</a><a href="#">CONTACT</a>
  </nav>
</header>

<section class="hero">
  <div class="abs" style="inset:0" role="img" aria-label="Boat deck finished with grey granulated rubber flooring"></div>
  <div class="hero-shade"></div>
  <h1 class="hero-title">Is it Time to Replace that Worn Out, Old and Faded Carpet in Your Boat?</h1>
  <a class="btn" href="#">CONTACT US</a>
  <span class="hero-arrow prev"><svg width="33" height="33" viewBox="0 0 33 33" fill="none" stroke="#fff" stroke-width="1.5"><path d="M19 11l-5 5.5 5 5.5"/></svg></span>
  <span class="hero-arrow next"><svg width="33" height="33" viewBox="0 0 33 33" fill="none" stroke="#4b525b" stroke-width="1.5"><path d="M14 11l5 5.5-5 5.5"/></svg></span>
  <div class="hero-dots"><i></i><i class="on"></i><i></i><i></i><i></i></div>
</section>

<section class="welcome">
  <span class="eyebrow" style="left:110px;top:770px">WELCOME TO KEEL-DECK</span>
  <h2 class="welcome-h">Keel-Deck is High Performance Marine Surfacing!<span class="rule"></span></h2>
  <h3 class="welcome-sub">Keel-Deck is a Recycled Granulated Rubber Flooring!</h3>
  <p class="welcome-p">That is chemically bonded to your boat deck, patio, or any other surface to create an easy to clean, durable, great looking custom surface with unrivaled slip-resistance. Do not spend your hard earned money on surfacing that you will have to replace in a few years ...</p>
  <a class="link-more" style="left:110px;top:1204px" href="#">DISCOVER MORE ABOUT</a>
  <div class="welcome-frame"></div>
  <div class="welcome-photo" role="img" aria-label="Center console boat with grey rubber deck surfacing"></div>
</section>

<section class="stats">
  <div class="stat"><b>20</b><span>YEAR OF EXPERIENCE</span></div>
  <div class="stat"><b>580</b><span>COMPLETED PROJECTS</span></div>
  <div class="stat"><b>30+</b><span>EXPERIENCE WORKER</span></div>
</section>

<section class="services">
  <span class="eyebrow" style="left:110px;top:1530px">WHAT WE DO</span>
  <h2 class="sec-title" style="left:110px;top:1556px">Our Services</h2>
  <a class="link-more" style="left:963px;top:1562px" href="#">VIEW ALL SERVICES</a>

  <article class="service service-marine">
    <div class="photo" role="img" aria-label="Bass boat with slip resistant rubber flooring on deck"></div>
    <div class="panel">
      <span class="tag" style="left:56px;top:38px">MARINE FLOORING</span>
      <h3 style="left:56px;top:80px;width:400px">Our product is the ultimate in slip resistant flooring</h3>
      <p style="left:56px;top:158px;width:390px">Is it time to replace that worn out, old and faded carpet in your boat? Tired of your carpet releasing from the deck? Tired of the constant uncertainty when boarding your boat? Disappointed with the ...</p>
      <a class="link-more" style="left:56px;top:290px" href="#">MORE DETAILS</a>
    </div>
    <span class="connector"></span>
  </article>

  <article class="service service-residential">
    <div class="panel">
      <span class="tag" style="left:300px;top:40px">RESIDENTIAL FLOORING</span>
      <h3 style="left:80px;top:80px;width:380px;text-align:right">Is bringing the best slip resistance straight to your home!</h3>
      <p style="left:80px;top:158px;width:380px">Add a custom look to your patio, deck or any place you would like that will increase your homes value along with reducing those high insurance rates by decreasing the possibility of a slip ...</p>
      <a class="link-more" style="left:360px;top:280px" href="#">MORE DETAILS</a>
    </div>
    <div class="photo" role="img" aria-label="Home deck with rubber surface and black metal railing"></div>
  </article>
</section>

<section class="gallery">
  <span class="eyebrow" style="left:110px;top:2474px">PHOTO GALLERY</span>
  <h2 class="sec-title" style="left:110px;top:2500px">Latest Projects</h2>
  <a class="link-more" style="left:960px;top:2506px" href="#">VIEW ALL PROJECTS</a>
  <div class="proj proj-left" role="img" aria-label="Residential railing over rubber surfaced deck"></div>
  <div class="proj proj-main">
    <div class="abs" style="inset:0" role="img" aria-label="Boat deck with green rubber flooring panels"></div>
    <div class="shade"></div>
    <span class="cat">MARINE FLOORING</span>
    <h4>Slip resistant rubberized<br>flooring</h4>
    <span class="plus"><svg width="31" height="31" viewBox="0 0 31 31" stroke="#fff" stroke-width="1.5"><path d="M15.5 10v11M10 15.5h11"/></svg></span>
  </div>
  <div class="proj proj-right" role="img" aria-label="Light grey rubber boat deck"></div>
</section>

<section class="cta">
  <p class="cta-text">Is it time to replace<br>that worn out, old and faded carpet in your boat?</p>
  <a class="cta-btn" href="#">CONTACT NOW!</a>
</section>

<section class="testimonials">
  <span class="eyebrow">TESTIMONIALS</span>
  <h2>Client Love Our Work</h2>
  <blockquote>I spent many weeks looking for a deck coating that met all my specifications. Color and slip prevention were important but I was also looking for something that offered anti fatigue properties.</blockquote>
  <div class="author">
    <svg width="12" height="10" viewBox="0 0 12 10" fill="none" stroke="#d5d5d5"><path d="M12 5H1M5 1L1 5l4 4"/></svg>
    <span class="dash"></span><span>DALE HOLLINS</span><span class="dash"></span>
    <svg width="12" height="10" viewBox="0 0 12 10" fill="none" stroke="#d5d5d5"><path d="M0 5h11M7 1l4 4-4 4"/></svg>
  </div>
  <a class="view-all" href="#">VIEW ALL TESTIMONIALS</a>
</section>

<section class="links">
  <div class="links-rule"></div>
  <span class="links-label">LINKS</span>
  <h2 class="links-title">We Like</h2>
  <div class="partner partner-a"></div>
  <div class="partner partner-b"></div>
  <div class="partner partner-c"></div>
</section>

<footer class="site-footer">
  <span class="foot-brand"><i></i>Keel-Deck</span>
  <nav class="foot-nav"><a href="#">ABOUT</a><a href="#">MARINE</a><a href="#">RESIDENTIAL</a><a href="#">PHOTOS</a><a href="#">FAQS</a><a href="#">LINKS</a><a href="#">CONTACT</a></nav>
  <a class="social" href="https://www.facebook.com/keeldeckexample" aria-label="Social page"></a>
  <div class="foot-rule"></div>
  <p class="copyright">©2018 <b>Keel-Deck LLC.</b> All Rights Reserved</p>
  <a class="directions" href="#">GET DIRECTIONS</a>
  <svg class="to-top" viewBox="0 0 24 24" fill="none" stroke="#0692cd" stroke-width="2"><path d="M12 20V5M6 11l6-6 6 6"/></svg>
</footer>

</body>
</html>
```